IT Support Business needs a Flyer Designed

Have just had new logo and business cards made for new business called Orbit Logic, am now in need of a new flyer design. Orbit Logic will be providing home and small business it support.
Orbit Logic flyer design brief has been uploaded. The contest has also been changed to payment guaranteed.
If you need anymore information please feel free to contact myself.
Reason: I signed up early to take advantage of the artbazaar 24 hour sale, and was a few days late in providing a design brief. Therefore I am extending the deadline by 2 days, to ensure it lasts for a good 2 weeks.
Have worked on and refined the Design Brief a bit more, hoping it makes it a bit clearer as to what I want on the flyer. If you have any questions please do not hesitate to ask.
I have refined the design brief overnight, after receiving some feedback, please refer to newly uploaded file for this morning. I am hoping it makes things clearer and easier.
Small Business

```html
<!DOCTYPE html>
<html lang="en">
<head>
<meta charset="utf-8">
<title>Orbit Logic Flyer</title>
<link rel="stylesheet" href="https://fonts.googleapis.com/css2?family=Open+Sans:wght@400;600;700;800&display=swap">
<style>
  :root {
    --blue: #1f4f9c;
    --blue-dark: #173a78;
    --blue-light: #3d79c9;
    --red: #e0342c;
    --ink: #2b2b2b;
    --paper: #ffffff;
    --mist: #e9ecef;
    --photo-warm: #b89a80;
    --photo-cool: #8fa6b8;
  }
  * { box-sizing: border-box; margin: 0; padding: 0; }
  html, body { width: 857px; height: 1200px; overflow: hidden; background: var(--paper); }
  body { font-family: "Open Sans", Arial, sans-serif; color: var(--ink); }
  .flyer { position: relative; width: 857px; height: 1200px; overflow: hidden;
    background: linear-gradient(180deg, var(--paper) 0%, var(--paper) 55%, var(--mist) 100%); }

  .brand { position: absolute; top: 30px; left: 0; width: 100%; display: flex; justify-content: center; align-items: center; gap: 14px; }
  .brand-dot { width: 46px; height: 46px; border-radius: 50%; background: var(--red); }
  .brand-name { font-size: 50px; font-weight: 800; color: var(--blue); letter-spacing: 1px; text-transform: uppercase; line-height: 1.2; }

  .tagline { position: absolute; top: 130px; width: 100%; text-align: center; color: var(--red); font-weight: 700; font-size: 21px; }
  .intro { position: absolute; top: 166px; left: 110px; width: 637px; text-align: center; font-size: 17px; line-height: 1.4; }

  .hero { position: absolute; top: 250px; left: 0; width: 857px; height: 440px; }
  .hero-photo { position: absolute; top: 22px; left: 0; width: 857px; height: 370px;
    background: linear-gradient(120deg, var(--photo-warm) 0%, #d9c8b4 45%, var(--photo-cool) 100%); }
  .hero-swoosh { position: absolute; left: 0; width: 857px; }
  .hero-swoosh.top { top: 0; height: 60px; }
  .hero-swoosh.bottom { top: 350px; height: 80px; }

  .spot { position: absolute; border-radius: 50%; border: 6px solid var(--red); background: linear-gradient(135deg, var(--photo-cool), var(--photo-warm)); }
  .spot.left { left: 248px; top: 595px; width: 125px; height: 125px; border-color: var(--blue-light); }
  .spot.center { left: 354px; top: 555px; width: 150px; height: 150px; }
  .spot.right { left: 485px; top: 595px; width: 125px; height: 125px; border-color: var(--blue-light); }

  .skills-head { position: absolute; top: 738px; left: 250px; width: 357px; height: 40px; border-radius: 20px;
    background: linear-gradient(180deg, var(--blue-light), var(--blue)); color: var(--paper);
    font-weight: 700; font-size: 19px; display: flex; align-items: center; justify-content: center; }
  .skills { position: absolute; top: 792px; left: 80px; width: 700px; display: grid; grid-template-columns: 1fr 1fr; column-gap: 30px; }
  .skills ul { list-style: none; }
  .skills li { position: relative; padding-left: 26px; color: var(--blue); font-size: 17px; line-height: 1.25; margin-bottom: 8px; }
  .skills li::before { content: ""; position: absolute; left: 0; top: 5px; border-left: 14px solid var(--red); border-top: 7px solid transparent; border-bottom: 7px solid transparent; }

  .details { position: absolute; top: 1000px; left: 78px; width: 700px; text-align: center; font-size: 13px; line-height: 1.3; }
  .details p { margin-bottom: 6px; }

  .footer-swoosh { position: absolute; top: 1112px; left: 0; width: 857px; height: 40px; }
  .contact-bar { position: absolute; top: 1148px; left: 0; width: 857px; height: 52px; background: var(--blue-dark);
    display: flex; align-items: center; justify-content: center; gap: 60px; color: var(--paper); font-weight: 700; font-size: 28px; }
  .contact-item { display: flex; align-items: center; gap: 10px; }
  .contact-item svg { width: 28px; height: 28px; }
</style>
</head>
<body>
<main class="flyer">
  <header class="brand">
    <span class="brand-dot"></span>
    <span class="brand-name">Orbit Logic</span>
  </header>

  <p class="tagline">Providing solutions for all your computer and technical equipment needs.</p>
  <p class="intro">With over 15 years experience in the IT sector, Daniel from Orbit Logic provides friendly, reliable and professional service, supporting you to build your skills and knowledge to maximise your IT requirements.</p>

  <section class="hero">
    <div class="hero-photo" role="img" aria-label="Photo of a smiling couple working together at a laptop at home"></div>
    <svg class="hero-swoosh top" viewBox="0 0 857 60" preserveAspectRatio="none">
      <path d="M0 0 H857 V10 Q430 70 0 20 Z" fill="#ffffff"/>
      <path d="M0 20 Q430 70 857 10 V18 Q430 78 0 28 Z" fill="#1f4f9c"/>
      <path d="M0 28 Q430 78 857 18 V22 Q430 82 0 32 Z" fill="#e0342c"/>
    </svg>
    <svg class="hero-swoosh bottom" viewBox="0 0 857 80" preserveAspectRatio="none">
      <path d="M0 40 Q430 -10 857 40 V80 H0 Z" fill="#ffffff"/>
      <path d="M0 30 Q430 -20 857 30 V40 Q430 -10 0 40 Z" fill="#1f4f9c"/>
      <path d="M0 24 Q430 -26 857 24 V30 Q430 -20 0 30 Z" fill="#e0342c"/>
    </svg>
  </section>

  <div class="spot left" role="img" aria-label="Photo of a technician repairing a computer"></div>
  <div class="spot right" role="img" aria-label="Photo of a person using a laptop"></div>
  <div class="spot center" role="img" aria-label="Photo of a consultant helping a client at a computer"></div>

  <h2 class="skills-head">Orbit Logic specialises in:</h2>
  <div class="skills">
    <ul>
      <li>Computer repair, service, installation and upgrades.</li>
      <li>Support to set up and secure your home network.</li>
      <li>Sharing the tricks and tips to manage your new operating system.</li>
      <li>Assistance in installing and configuring new software.</li>
    </ul>
    <ul>
      <li>Getting you connected online and across social media faster, including Internet, email, Chatwave, Friendspace etc.</li>
      <li>Data backup and recovery.</li>
      <li>Tuition in programs and technology.</li>
    </ul>
  </div>

  <section class="details">
    <p>Our services and expertise extends across PC's, Laptops, printers, scanners, routers, tablet, mobile phone, cameras, television and arcade consoles, with the ability to work onsite or remotely as required.</p>
    <p>Orbit Logic service fees start at $40 per hour however packages and flexible pricing for more complex tasks are available.</p>
    <p>With no call out fee, talk to Daniel today to solve your IT and technology challenges.</p>
  </section>

  <svg class="footer-swoosh" viewBox="0 0 857 40" preserveAspectRatio="none">
    <path d="M0 22 Q430 -6 857 22 V40 H0 Z" fill="#e0342c"/>
    <path d="M0 30 Q430 2 857 30 V40 H0 Z" fill="#1f4f9c"/>
  </svg>
  <footer class="contact-bar">
    <span class="contact-item">
      <svg viewBox="0 0 24 24"><path fill="#ffffff" d="M6.6 10.8a15 15 0 0 0 6.6 6.6l2.2-2.2a1 1 0 0 1 1-.25 11.4 11.4 0 0 0 3.6.57 1 1 0 0 1 1 1V20a1 1 0 0 1-1 1A17 17 0 0 1 3 4a1 1 0 0 1 1-1h3.5a1 1 0 0 1 1 1c0 1.25.2 2.45.57 3.57a1 1 0 0 1-.25 1z"/></svg>
      0400 123 987
    </span>
    <span class="contact-item">
      <svg viewBox="0 0 24 24"><rect x="2" y="5" width="20" height="14" rx="2" fill="#ffffff"/><path d="M3 6l9 7 9-7" stroke="#173a78" stroke-width="2" fill="none"/></svg>
      daniel@orbitlogic.example
    </span>
  </footer>
</main>
</body>
</html>
```